Silver MarlinJuice Company from Germany needs a Web Design

Hey Guys,

We need a Great Web Design I Hope we get nice Designs.
I put our company Logo in the Files.
Our Juice is Very Healthy and we don't use Sugar or other stuff it's 100% Natural Juice.
We are a German Company
Updates

I have a good Design already , but when someone works on a design, i will wait until you send it to me.

Industry/Entity Type

It Company

Coding

Coded - Design and coding required

Number of Pages Required

1 page

Requirements
Must have
• It has to be something with Vegetables: Apple, Carrots, courgette, fennel, beetroot, orange, salads, lemons, nettle. We producing the juice with these Vegetables and fruits.
Nice to have
• I Put a couple designs in the files i like Designs ,when you go on a Website and you are not confused :)

```html
<!DOCTYPE html>
<html lang="en">
<head>
<meta charset="utf-8">
<title>Silver Marlin Juice</title>
<link href="https://fonts.googleapis.com/css2?family=Roboto+Slab:wght@400;700&family=Open+Sans:wght@400;600&display=swap" rel="stylesheet">
<style>
:root{
  --green:#1e9e4a;
  --green-dark:#17863d;
  --lime:#7cc143;
  --lime-dark:#5f9e2e;
  --field:#5ed38a;
  --field-border:#8de6ad;
  --white:#ffffff;
  --ink:#333333;
  --gallery-bg:#eef0ee;
}
*{box-sizing:border-box;margin:0;padding:0}
html,body{width:773px;height:1200px;overflow:hidden}
body{position:relative;font-family:"Open Sans",sans-serif;color:var(--ink);background:var(--white)}
.abs{position:absolute}
h2,h3{font-family:"Roboto Slab",serif;font-weight:400}

.hero-backdrop{left:0;top:0;width:773px;height:483px;
  background:linear-gradient(90deg,#5f7f34 0%,#8aa545 6.7%,#c9b45a 50%,#d9893a 93%,#a8552a 100%)}

.site-header{left:52px;top:38px;width:670px;height:132px;background:var(--white)}
.brand{left:0;top:26px;width:670px;display:flex;justify-content:center;align-items:center;gap:8px}
.brand-dot{width:14px;height:14px;border-radius:50%;background:var(--lime)}
.brand-name{font-family:"Roboto Slab",serif;font-size:18px;color:var(--green)}
.main-nav{left:0;top:106px;width:670px;display:flex;justify-content:center}
.main-nav a{font-size:8px;letter-spacing:.8px;text-transform:uppercase;color:var(--ink);text-decoration:none;padding:0 12px;border-left:1px solid #ccc}
.main-nav a:first-child{border-left:none}

.slider{left:52px;top:170px;width:450px;height:310px;
  background:linear-gradient(90deg,#a81f35 0%,#c93a3a 18%,#e98a1f 42%,#e2b63a 68%,#b9c95a 100%)}
.slider-arrow{top:140px;width:22px;height:22px;border-radius:50%;background:rgba(255,255,255,.8)}
.slider-arrow svg{display:block;margin:6px auto}
.slide-info{left:502px;top:170px;width:220px;height:310px;background:var(--lime);color:var(--white);padding:40px 26px 0}
.slide-info h2{font-size:21px;line-height:1.2;margin-bottom:12px}
.slide-info p{font-size:7.5px;line-height:1.6;margin-bottom:18px}
.btn{display:inline-block;font-size:9px;color:var(--white);text-decoration:none;padding:7px 14px}
.btn-olive{background:var(--lime-dark)}
.btn-dark{background:var(--green-dark);border:1px solid rgba(255,255,255,.4)}

.fresh{left:0;top:483px;width:773px;height:212px;background:var(--green);color:var(--white)}
.fresh-copy{left:52px;top:32px;width:380px}
.fresh-copy h2{font-size:20px;font-weight:700;margin-bottom:10px}
.fresh-copy p{font-size:7.5px;line-height:1.6;margin-bottom:14px}
.rule{width:90px;height:2px;background:var(--white);margin-bottom:14px}
.fresh-fruit{left:462px;top:30px;width:260px;height:155px;border-radius:12px;
  background:linear-gradient(135deg,#f2b24a 0%,#ee7a2c 45%,#d9452f 75%,#8fb240 100%)}

.feature-row{left:0;top:695px;width:773px;height:210px;background:var(--white)}
.carrot-photo{left:52px;top:0;width:296px;height:210px;background:linear-gradient(135deg,#f1a03a 0%,#e46d22 55%,#c65b20 100%)}
.gallery{left:348px;top:0;width:374px;height:210px;background:var(--gallery-bg)}
.gallery h3{position:absolute;left:167px;top:16px;font-size:17px}
.thumbs{position:absolute;left:33px;top:50px;width:341px;display:grid;grid-template-columns:repeat(3,1fr);gap:10px 12px}
.thumb{height:68px}
.t1{background:linear-gradient(135deg,#d66a2b,#f2b44a)}
.t2{background:linear-gradient(135deg,#e9c13a,#f7e27a)}
.t3{background:linear-gradient(135deg,#b72a3a,#e0783c)}
.t4{background:linear-gradient(135deg,#8fb845,#e6a23a)}
.t5{background:linear-gradient(135deg,#f19a2e,#f6d06a)}
.t6{background:linear-gradient(135deg,#c43540,#d98a3a)}

.site-footer{left:0;top:905px;width:773px;height:295px;background:var(--green);color:var(--white)}
.site-footer h3{font-family:"Open Sans",sans-serif;font-size:11px;font-weight:600;letter-spacing:.5px;text-transform:uppercase}
.contact{left:52px;top:22px;width:370px}
.contact-form{margin-top:14px;display:grid;grid-template-columns:1fr 1fr;gap:10px 14px}
.field{height:20px;background:var(--field);border:1px solid var(--field-border);font-size:7px;color:var(--white);padding:5px 6px}
.field-message{grid-column:1/3;height:90px}
.submit-row{left:52px;top:235px;display:flex;align-items:center;gap:14px}
.submit{background:var(--green-dark);border:1px solid rgba(255,255,255,.35);font-size:8px;padding:10px 22px;color:var(--white)}
.copyright{font-size:7px}
.location{left:512px;top:22px;width:210px}
.map{margin-top:12px;width:210px;height:105px;background:linear-gradient(135deg,#eef1ec,#d9dfd6)}
.socials{margin-top:10px;display:flex;gap:6px}
.social{width:13px;height:13px;border-radius:50%}
.s1{background:#3b5998}.s2{background:#55acee}.s3{background:#dd4b39}.s4{background:#e4405f}
.contact-list{margin-top:10px;list-style:none;font-size:7.5px;line-height:1.4}
.contact-list li{display:flex;gap:7px;margin-bottom:6px;align-items:flex-start}
.contact-list svg{flex:none}
</style>
</head>
<body>

<div class="abs hero-backdrop" role="img" aria-label="Fresh fruit and vegetables on a wooden table"></div>

<header class="abs site-header">
  <div class="abs brand"><span class="brand-dot"></span><span class="brand-name">Silver Marlin Juice</span></div>
  <nav class="abs main-nav">
    <a href="#">Home</a><a href="#">About</a><a href="#">Portfolio</a><a href="#">Store</a><a href="#">Blog</a><a href="#">Contacts</a>
  </nav>
</header>

<div class="abs slider" role="img" aria-label="Red, orange and yellow juice being poured into glasses">
  <span class="abs slider-arrow" style="left:10px"><svg width="8" height="10" viewBox="0 0 8 10"><path d="M6 1L2 5l4 4" stroke="#555" stroke-width="1.6" fill="none"/></svg></span>
  <span class="abs slider-arrow" style="right:10px"><svg width="8" height="10" viewBox="0 0 8 10"><path d="M2 1l4 4-4 4" stroke="#555" stroke-width="1.6" fill="none"/></svg></span>
</div>
<section class="abs slide-info">
  <h2>Highest Quality Juice</h2>
  <p>Pressed fresh every morning from ripe fruit and garden vegetables, with no added sugar, no water and nothing artificial in every single bottle.</p>
  <a class="btn btn-olive" href="#">Know More</a>
</section>

<section class="abs fresh">
  <div class="abs fresh-copy">
    <h2>100 % Fresh and Natural</h2>
    <p>Apples, carrots, beetroot, fennel, lemons and nettle go straight from the field into the press. We keep every vitamin in and leave everything else out, so each glass tastes the way nature made it.</p>
    <div class="rule"></div>
    <a class="btn btn-dark" href="#">Know about us</a>
  </div>
  <div class="abs fresh-fruit" role="img" aria-label="Glasses of juice with oranges, grapefruit and strawberries"></div>
</section>

<section class="abs feature-row">
  <div class="abs carrot-photo" role="img" aria-label="Glass of carrot juice beside fresh carrots"></div>
  <div class="abs gallery">
    <h3>Gallery</h3>
    <div class="thumbs">
      <div class="thumb t1" role="img" aria-label="Orange juice glass"></div>
      <div class="thumb t2" role="img" aria-label="Lemon slices"></div>
      <div class="thumb t3" role="img" aria-label="Berry juice"></div>
      <div class="thumb t4" role="img" aria-label="Fruit mix"></div>
      <div class="thumb t5" role="img" aria-label="Orange juice bottles"></div>
      <div class="thumb t6" role="img" aria-label="Beetroot juice"></div>
    </div>
  </div>
</section>

<footer class="abs site-footer">
  <div class="abs contact">
    <h3>Contact Us</h3>
    <div class="contact-form">
      <div class="field">Name</div>
      <div class="field">Email Address</div>
      <div class="field">Contact Number</div>
      <div class="field">Subject</div>
      <div class="field field-message">Your message</div>
    </div>
  </div>
  <div class="abs submit-row">
    <span class="submit">SUBMIT</span>
    <span class="copyright">Copyright 2021 Silver Marlin. All Rights Reserved.</span>
  </div>
  <div class="abs location">
    <h3>Location</h3>
    <div class="map" role="img" aria-label="Street map showing the company location"></div>
    <div class="socials"><span class="social s1"></span><span class="social s2"></span><span class="social s3"></span><span class="social s4"></span></div>
    <ul class="contact-list">
      <li><svg width="8" height="10" viewBox="0 0 8 10"><path d="M4 0a3.5 3.5 0 0 0-3.5 3.5C.5 6 4 10 4 10s3.5-4 3.5-6.5A3.5 3.5 0 0 0 4 0z" fill="#fff"/><circle cx="4" cy="3.5" r="1.2" fill="#1e9e4a"/></svg>14 Lindenweg, 20095 Hamburg, Germany</li>
      <li><svg width="9" height="9" viewBox="0 0 9 9"><path d="M2 0l1.6 2.3-1 1a5 5 0 0 0 3.1 3.1l1-1L9 7l-1 2C4 9 0 5 0 1z" fill="#fff"/></svg>+49 40 555 0187</li>
      <li><svg width="10" height="8" viewBox="0 0 10 8"><rect width="10" height="8" fill="#fff"/><path d="M0 0l5 4 5-4" stroke="#1e9e4a" fill="none"/></svg>hello@silvermarlinjuice.de</li>
    </ul>
  </div>
</footer>

</body>
</html>
```